New Full Color Flyer for Mailing Program

I have a flyer already for a program I launching. I am in need of a professional to use my flyer to create a much more leaner flyer. The new flyer should convey a message through the use of graphics rather then words.
The goal is to incite the reader to get excited and buy in, but at the same time explain the products that are included with a purchase.
Attached is my own flyer to be used as a reference point. I allow you to make suggestions to me to consider for the flyer and changes you think will perform well.
MUST BE PSD SOURCE & is expected to be handed over at the end.
Target Market(s)
Home business and income opportunity buyers
Industry/Entity Type
Small Business
Colors
Designer to choose colors to be used in the design.
Requirements
Must have
- Exciting Graphics/cartoons that convey success, money and riches. Should look good in color and gray/white.
- Level Payouts
- Order Form
- THE KESTREL VALE ROUTINE
Nice to have
- crisp clean text

```html
<!DOCTYPE html>
<html lang="en">
<head>
<meta charset="utf-8">
<title>Kestrel Vale Routine Flyer</title>
<link rel="stylesheet" href="https://fonts.googleapis.com/css2?family=Barlow:ital,wght@0,400;0,500;0,600;0,700;0,800;1,800&display=swap">
<style>
:root{
  --red:#c61f2d;
  --navy:#1c2443;
  --frame:#3d3d3f;
  --paper:#ececee;
  --paper-light:#f7f7f8;
  --ink:#1c2443;
  --muted:#8a8a8e;
  --line:#6c6c70;
  --white:#ffffff;
}
*{margin:0;padding:0;box-sizing:border-box}
html,body{width:934px;height:1200px;overflow:hidden;background:var(--frame)}
body{font-family:"Barlow",Arial,sans-serif;color:var(--ink)}
.flyer{position:relative;width:934px;height:1200px;background:var(--frame)}
.abs{position:absolute}
.sheet{left:35px;top:43px;width:863px;height:1114px;
  background:linear-gradient(180deg,var(--paper-light) 0%,var(--paper) 60%,#e4e4e6 100%)}

.header{left:35px;top:43px;width:863px;height:125px;background:var(--red);color:var(--white)}
.header h1{position:absolute;left:37px;top:22px;font-weight:700;font-size:54px;line-height:1;letter-spacing:.5px;white-space:nowrap}
.header p{position:absolute;left:38px;top:82px;font-weight:700;font-size:25px;line-height:1;letter-spacing:.3px}
.flag{left:686px;top:43px;width:212px;height:111px;
  background:linear-gradient(160deg,#2b3a78 0%,#9aa3c4 30%,#f2f2f2 50%,#c94050 75%,#f2f2f2 100%);opacity:.9}

.headline{left:35px;width:863px;text-align:center;line-height:1;white-space:nowrap}
.headline.l1{top:178px;font-weight:800;font-size:45px;letter-spacing:.5px}
.headline.l1 span{color:var(--red)}
.headline.l2{top:218px;font-weight:800;font-style:italic;font-size:41px;letter-spacing:.3px}

.intro{left:58px;top:273px;width:452px;font-size:16px;line-height:19px;color:var(--red)}
.intro b{font-weight:700}
.limits{left:58px;top:396px;font-weight:700;font-size:28px;line-height:31px;white-space:nowrap}
.look{left:58px;top:473px;font-weight:700;font-size:15.5px;line-height:23px;color:var(--red)}
.big-arrow{left:269px;top:485px}
.levels{left:344px;top:466px;font-weight:700;font-size:15px;line-height:19.6px;color:var(--red)}

.payplan{left:537px;top:262px;width:345px;height:301px;background:var(--navy);color:var(--white);padding:13px 16px}
.payplan h2{font-weight:700;font-size:31px;letter-spacing:.4px;line-height:1}
.payplan p{margin-top:10px;font-size:16px;line-height:19px}
.perks{list-style:none;margin-top:6px}
.perks li{display:flex;align-items:center;gap:8px;font-weight:700;font-size:16.5px;line-height:22.4px;white-space:nowrap}

.start{left:46px;top:571px;width:287px;height:471px;background:var(--red);color:var(--white);padding:12px 12px}
.start h2{font-weight:800;font-size:32px;line-height:33.6px;letter-spacing:.2px}
.start .select{margin-top:6px;font-weight:700;font-size:16px;line-height:20px;padding-bottom:2px;border-bottom:2px solid var(--white);white-space:nowrap}
.tier{margin-top:9px}
.tier h3{font-weight:700;font-size:15.5px;line-height:19px;white-space:nowrap}
.tier p{font-size:15.5px;line-height:18.7px;opacity:.92}
.start .note{margin-top:5px;font-weight:700;font-size:9.5px;white-space:nowrap}

.questions{left:46px;top:1046px;width:291px;text-align:center}
.questions strong{display:block;font-weight:800;font-size:40px;line-height:40px;color:var(--navy)}
.questions span{display:block;font-weight:700;font-size:15px;line-height:17px;color:var(--red)}
.leads{left:46px;top:1107px;width:291px;height:21px;background:var(--red);color:var(--white);font-weight:700;font-size:14.5px;text-align:center;line-height:21px}

.banner{left:343px;top:576px}
.banner-text{left:343px;top:576px;width:539px;height:26px;text-align:center;color:var(--white);font-weight:700;font-size:21px;line-height:26px;letter-spacing:.3px;white-space:nowrap}
.includes{left:345px;top:608px;width:539px;height:78px;border:2px dashed var(--navy);text-align:center;color:var(--red);font-weight:700;font-size:17.5px;line-height:22.4px;padding-top:5px}
.includes .row1{display:flex;justify-content:space-around}

.reports-title{left:444px;top:700px;width:324px;height:42px;background:var(--navy);color:var(--white);font-weight:700;font-size:31px;text-align:center;line-height:42px;letter-spacing:.4px}
.report h4{color:var(--red);font-weight:700;font-size:13px;line-height:16px;white-space:nowrap}
.report p{font-size:13.5px;line-height:16px;font-weight:500;white-space:nowrap}
.r1{left:348px;top:752px}.r2{left:597px;top:752px}
.r3{left:348px;top:792px}.r4{left:597px;top:792px}
.r5{left:345px;top:836px;width:539px;text-align:center}

.order{left:343px;top:882px;width:542px;height:247px;border:2px dashed var(--red)}
.order > *{position:absolute}
.order h4{left:12px;top:12px;color:var(--red);font-weight:700;font-size:14.5px;white-space:nowrap}
.joins{font-size:11px;font-weight:600;line-height:14px;white-space:nowrap}
.joins.dim{color:var(--muted);font-weight:500}
.j1{left:12px;top:37px}.j2{left:276px;top:37px}
.j3{left:12px;top:53px}.j4{left:276px;top:53px}
.j5{left:0;width:538px;top:69px;text-align:center}
.members{left:12px;top:90px;list-style:none;font-weight:700;font-size:15px;line-height:21.2px;white-space:nowrap}
.fields{left:12px;font-size:10.5px;font-weight:600;line-height:14px;color:var(--line);white-space:nowrap}
.f1{top:200px}.f2{top:218px}
.fields .line{display:inline-block;border-bottom:1px solid var(--line);height:10px}

.disclaimer{left:52px;top:1133px;width:520px;font-size:9px;line-height:10.5px;color:#333}
.copyright{left:642px;top:1138px;font-size:9px;color:#333;white-space:nowrap}
</style>
</head>
<body>
<div class="flyer">
  <div class="abs sheet"></div>

  <header class="abs header">
    <h1>KESTREL VALE ROUTINE</h1>
    <p>QUICK &amp; SIMPLE CASH GENERATOR!</p>
  </header>
  <div class="abs flag" role="img" aria-label="Waving flag in red, white and blue"></div>

  <div class="abs headline l1">GENERATE A <span>TSUNAMI</span> OF $500+</div>
  <div class="abs headline l2">CASH &amp; MONEY ORDER PAYMENTS DAILY</div>

  <p class="abs intro"><b>KESTREL VALE ROUTINE</b> is an exciting program paying <b>UNLIMITED</b> commissions to businesses and ordinary Joes around the country to resell our online profits how-to reports &amp; training manuals. You just mail this flyer and collect the direct payments. If you can mail a flyer, this is for you...do not miss this opportunity!</p>

  <h2 class="abs limits">The KESTREL VALE ROUTINE<br>Limits are ENDLESS!!!</h2>

  <p class="abs look">LOOK!!! The $500 Program<br>rewards handsomly.<br>Based on 10 who get 10</p>
  <svg class="abs big-arrow" width="64" height="52" viewBox="0 0 64 52" aria-hidden="true"><path d="M0 16H36V0L64 26L36 52V36H0Z" fill="#c61f2d"/></svg>
  <p class="abs levels">Level 1 = $5,000<br>Level 2 = $50,000<br>Level 3 = $500,000<br>Level 4 = $5,000,000</p>

  <section class="abs payplan">
    <h2>ENDLESS PAY PLAN</h2>
    <p>You are paid commissions on 4 Levels and your name will continue to be put onto your teams flyers through infinity. Your talking THOUSANDS of flyers with your name making you CASH...That is Power!!!</p>
    <ul class="perks">
      <li><svg width="19" height="13" viewBox="0 0 19 13"><path d="M0 4H10V0L19 6.5L10 13V9H0Z" fill="#fff"/></svg>Affordable Income Opportunity</li>
      <li><svg width="19" height="13" viewBox="0 0 19 13"><path d="M0 4H10V0L19 6.5L10 13V9H0Z" fill="#fff"/></svg>Company Support</li>
      <li><svg width="19" height="13" viewBox="0 0 19 13"><path d="M0 4H10V0L19 6.5L10 13V9H0Z" fill="#fff"/></svg>Simple To Earn, No monthly fee</li>
      <li><svg width="19" height="13" viewBox="0 0 19 13"><path d="M0 4H10V0L19 6.5L10 13V9H0Z" fill="#fff"/></svg>Updated and Fresh Products</li>
      <li><svg width="19" height="13" viewBox="0 0 19 13"><path d="M0 4H10V0L19 6.5L10 13V9H0Z" fill="#fff"/></svg>Unlimited &amp; Direct Payments</li>
    </ul>
  </section>

  <section class="abs start">
    <h2>GET STARTED IN THE KESTREL VALE ROUTINE</h2>
    <div class="select">Select Your Commission Level</div>
    <div class="tier"><h3>THE KESTREL VALE ROUTINE</h3><p>Unlimited $25 Payments</p></div>
    <div class="tier"><h3>THE KESTREL VALE ROUTINE II</h3><p>Unlimited $50 Payments, Includes above level as well.</p></div>
    <div class="tier"><h3>THE KESTREL VALE ROUTINE III</h3><p>Unlimited $100 Payments, Includes above levels as well.</p></div>
    <div class="tier"><h3>THE KESTREL VALE ROUTINE IV</h3><p>Unlimited $250 Payments, Includes above levels as well.</p></div>
    <div class="tier"><h3>THE KESTREL VALE ROUTINE V</h3><p>Unlimited $500 Payments, Includes above levels as well.</p></div>
    <p class="note">You only earn commissions upto your purchased level.</p>
  </section>

  <div class="abs questions"><strong>Questions?</strong><span>TKVR@KestrelValeRoutine.com</span></div>
  <div class="abs leads">Fresh Leads Included - 100/level</div>

  <svg class="abs banner" width="539" height="26" viewBox="0 0 539 26" aria-hidden="true"><path d="M0 0H539L531 13L539 26H0L8 13Z" fill="#1c2443"/></svg>
  <div class="abs banner-text">YOUR PURCHASE INCLUDES THE FOLLOWING</div>
  <div class="abs includes">
    <div class="row1"><span>Fresh Mailing Names on Labels</span><span>Discounted Campaigns</span></div>
    <div>Marketing Kit &amp; Quarterly Newsletter</div>
    <div>License to resell Kestrel Vale Routine</div>
  </div>

  <div class="abs reports-title">REPORTS &amp; GUIDES</div>
  <div class="abs report r1"><h4>THE KESTREL VALE ROUTINE</h4><p>7 Ways to success while you sleep</p></div>
  <div class="abs report r2"><h4>THE KESTREL VALE ROUTINE II</h4><p>The Home Business Guru &amp; TKVR I report</p></div>
  <div class="abs report r3"><h4>THE KESTREL VALE ROUTINE III</h4><p>Your Money Mind &amp; TKVR I, 11 reports</p></div>
  <div class="abs report r4"><h4>THE KESTREL VALE ROUTINE IV</h4><p>List Building Madness &amp; TKVR I,11, III reports</p></div>
  <div class="abs report r5"><h4>THE KESTREL VALE ROUTINE V</h4><p>Socialnest Training Guide &amp; ALL TKVR reports</p></div>

  <section class="abs order">
    <h4>Send Your: Cash, Money Orders or Cashiers Check to The Below Members</h4>
    <span class="joins j1">Join System I &amp; send each person below $25</span>
    <span class="joins j2">Join System III &amp; send each person below $100</span>
    <span class="joins dim j3">Join System II &amp; send each person below $50</span>
    <span class="joins dim j4">Join System IV &amp; send each person below $250</span>
    <span class="joins j5">Join System V &amp; send each person below $500</span>
    <ol class="members">
      <li>1.) Daniel Marsh 118 Linden Ave, Harlow CT 06999 1-860-555-0142</li>
      <li>2.) Free Space. No Payment = You Save CASH! :)</li>
      <li>3.) Free Space. No Payment = You Save CASH! :)</li>
      <li>4.) Free Space. No Payment = You Save CASH! :)</li>
      <li>5.) Vale Mail Works, PO Box 210, Harlow CT 06999 1-866-555-0178</li>
    </ol>
    <div class="fields f1">Name <span class="line" style="width:175px"></span> Phone <span class="line" style="width:95px"></span> Include on Flyer (Circle One) yes/no</div>
    <div class="fields f2">Addr <span class="line" style="width:190px"></span> City <span class="line" style="width:55px"></span> State <span class="line" style="width:40px"></span> ZipCode <span class="line" style="width:65px"></span></div>
  </section>

  <p class="abs disclaimer">Disclaimer: Purchase is for reports, names and marketing kit and license to be a commissioned affiliate for this offer. Income example is for illustrative purposes only. No guaranteed income. Void where prohibited.</p>
  <p class="abs copyright">Copyright 2107 All Right Reserved Vale Mail Works</p>
</div>
</body>
</html>
```